Business Card Design EFTPOS Comparison site

At QuoteHarbor.com.au we are a free service that allows our customers to get up to five quotes from our panel of suppliers for a range of BUSINESS related products and services. These products include eftpos / credit card machines, bank accounts, insurance, signage,office furniture etc. basically anything that a small business would need.
The process is done in 3 steps; 1) register your enquiry 2) we source and provide the five cheapest quotes 3) then select the supplier of your choice,the process is simple ABC and is FREE.
Please visit the soon to be revamped website to see our logo.
Target Market(s)
Small business operators
Industry/Entity Type
Small Business
Requirements
Must have
- Double Sided card

```html
<!DOCTYPE html>
<html lang="en">
<head>
<meta charset="utf-8">
<title>QuoteHarbor Business Card</title>
<link rel="stylesheet" href="https://fonts.googleapis.com/css2?family=Arimo:wght@400;700&display=swap">
<style>
  :root {
    --backdrop: #2a2a2c;
    --card-blue: #24408f;
    --panel-blue: #243c86;
    --card-white: #f4f4f4;
    --frame-grey: #8f8f96;
    --ink-dark: #101522;
    --ink-light: #f2f4fa;
    --brand-orange: #ef8a1c;
  }
  * { margin: 0; padding: 0; box-sizing: border-box; }
  html, body {
    width: 1200px;
    height: 900px;
    overflow: hidden;
    background: var(--backdrop);
    font-family: "Arimo", Arial, sans-serif;
  }
  .stage { position: relative; width: 1200px; height: 900px; }

  .card {
    position: absolute;
    width: 520px;
    height: 300px;
    box-shadow: 0 18px 40px rgba(0,0,0,.55);
  }

  /* Front side */
  .card-front {
    left: 80px;
    top: 130px;
    background: var(--card-blue);
    padding: 20px;
  }
  .card-front .face {
    width: 100%;
    height: 100%;
    background: radial-gradient(ellipse at center, #ffffff 0%, #ececec 100%);
    border: 2px solid var(--frame-grey);
    display: flex;
    align-items: center;
    justify-content: center;
  }
  .brand {
    display: flex;
    align-items: center;
    gap: 12px;
    color: var(--brand-orange);
    font-weight: 700;
    font-size: 44px;
    letter-spacing: -0.5px;
  }
  .brand-dot {
    width: 34px;
    height: 34px;
    border-radius: 50%;
    background: var(--brand-orange);
  }

  /* Back side */
  .card-back {
    left: 600px;
    top: 470px;
    background: var(--card-white);
    padding: 24px;
  }
  .card-back .face {
    width: 100%;
    height: 100%;
    background: var(--panel-blue);
    border: 2px solid var(--frame-grey);
    position: relative;
  }
  .identity {
    position: absolute;
    left: 34px;
    top: 150px;
  }
  .person-name {
    font-weight: 700;
    font-size: 24px;
    letter-spacing: 0.5px;
    color: var(--ink-light);
  }
  .person-name .dark { color: var(--ink-dark); }
  .person-role {
    font-weight: 700;
    font-size: 17px;
    color: var(--ink-light);
    margin-top: 2px;
  }
  .divider {
    position: absolute;
    left: 262px;
    top: 44px;
    width: 1.5px;
    height: 150px;
    background: var(--ink-dark);
  }
  .contacts {
    position: absolute;
    left: 278px;
    top: 60px;
    list-style: none;
  }
  .contacts li {
    display: flex;
    align-items: center;
    gap: 8px;
    font-size: 13px;
    color: var(--ink-light);
    height: 21px;
  }
  .contacts svg { width: 12px; height: 12px; flex: none; }
</style>
</head>
<body>
<main class="stage">

  <section class="card card-front" aria-label="Card front">
    <div class="face">
      <div class="brand">
        <span class="brand-dot"></span>
        <span class="brand-name">QuoteHarbor</span>
      </div>
    </div>
  </section>

  <section class="card card-back" aria-label="Card back">
    <div class="face">
      <div class="identity">
        <p class="person-name"><span class="dark">YOUR N</span>AME</p>
        <p class="person-role">Company Position</p>
      </div>
      <div class="divider"></div>
      <ul class="contacts">
        <li>
          <svg viewBox="0 0 12 12"><circle cx="6" cy="6" r="5.5" fill="none" stroke="#101522"/><path d="M4 3.2l1 1.6-.6.6c.4.8 1 1.4 1.8 1.8l.6-.6 1.6 1-.6 1.2C5.6 8.6 3.4 6.4 3 4z" fill="#101522"/></svg>
          <span>000 123 4567</span>
        </li>
        <li>
          <svg viewBox="0 0 12 12"><path d="M6 1L.5 6H2v5h3V8h2v3h3V6h1.5z" fill="#101522"/></svg>
          <span>your address</span>
        </li>
        <li>
          <svg viewBox="0 0 12 12"><rect x="1" y="2.5" width="10" height="7" fill="none" stroke="#101522"/><path d="M1 2.5l5 4 5-4" fill="none" stroke="#101522"/></svg>
          <span>youremail@domain.com</span>
        </li>
        <li>
          <svg viewBox="0 0 12 12"><circle cx="6" cy="4" r="2.5" fill="#101522"/><path d="M6 6v5.5" stroke="#101522" stroke-width="1.2"/></svg>
          <span>QuoteHarbor.com.au</span>
        </li>
      </ul>
    </div>
  </section>

</main>
</body>
</html>
```